Design of slide which will later be converted to video

We need slides which will be converted to a video format for web and social media marketing. We are attaching our concept draft as a start

All slides are provided as background only at this point, but if someone has a great idea for any of the other topics, feel free to provide that as well.

Using the attached slides (11-15), please re-create the slides in a more artistic and unified presentation, using stock images of the dog characters (no animation). The Professor must be a Basset hound with glasses; the other dog characters should be similar to the ones used in the slides. Voices and music will be added later. Any detail that can be added to make the video a seamless narrative is encouraged.
Original source files for pics here: quillbarkhaus-my.fileshelf.example/:f:/p/trevor/Kx_R7TQWm_bPlDcVa-hRxZAqQv3Lseyfm9Tk04B7W1Nj?e=QWPLMA
Updates

We have updated our brief to include source files for our images. Many designers have asked for this. Please have a look!

Target Market(s)

Fresh Pet Food

Industry/Entity Type

Pet Food

Colors
EB3D1F
EC4F4E
F09395
F8D3D4
FCEDEE

Requirements
Must have
• We want to keep the picture of the basset hound with glasses. We can potentially use other pictures of the other dogs, but not necessary. All dogs must be real pictures, no animation! The chalkboard needs to be a chalkboard - do not change it to something else, but please feel free to improve its look. This improvement - to all of our graphics - is what we are looking for.
Nice to have
• The chalkboard text come in as being written in real time; the dog pictures selected can be changed as per the designder creative instincts. We are pretty committed to the Basset Hound playing Professor Wembleton, but we are always open to suggestion

```html
<!DOCTYPE html>
<html lang="en">
<head>
<meta charset="utf-8">
<title>Ask Professor Wembleton – Slide Set</title>
<link href="https://fonts.googleapis.com/css2?family=League+Gothic&family=Montserrat:wght@400;500;600&family=Caveat:wght@500&display=swap" rel="stylesheet">
<style>
  :root {
    --board-red: #a9221c;
    --brand-red: #b3211b;
    --ink-brown: #3d1510;
    --ink-dark: #1f1a19;
    --paper: #ffffff;
    --halo: #f1f1f1;
    --photo-warm: #b9825a;
    --photo-grey: #9a9490;
  }
  * { box-sizing: border-box; margin: 0; padding: 0; }
  html, body { width: 675px; height: 1200px; overflow: hidden; }
  body {
    position: relative;
    background: var(--board-red);
    font-family: "Montserrat", sans-serif;
    color: var(--ink-dark);
  }
  .board-note {
    position: absolute; top: 34px; left: 0; width: 675px;
    text-align: center; color: #fff; font-size: 17.5px; font-weight: 500; line-height: 21px;
  }
  .slide {
    position: absolute; background: var(--paper);
    box-shadow: 0 3px 10px rgba(0,0,0,.25);
    overflow: hidden;
  }
  .halo { position: absolute; border-radius: 50%; background: var(--halo); }
  .photo { position: absolute; }
  .brand {
    position: absolute; display: flex; align-items: center; gap: 4px;
    color: var(--brand-red); font-weight: 600;
  }
  .brand-dot { border-radius: 50%; border: 2px solid var(--brand-red); }
  .quote-mark { color: var(--brand-red); font-family: "League Gothic", sans-serif; position: absolute; line-height: 1; }
  .accent { color: var(--brand-red); }
  .display { font-family: "League Gothic", sans-serif; color: var(--ink-brown); font-weight: 400; white-space: nowrap; }

  /* Title slide */
  .slide-title { left: 85px; top: 114px; width: 489px; height: 271px; }
  .slide-title .brand { left: 124px; top: 58px; font-size: 13px; }
  .slide-title .brand-dot { width: 16px; height: 16px; }
  .slide-title h1 { position: absolute; left: 0; width: 308px; top: 104px; text-align: center; font-size: 36px; line-height: 38px; }
  .topic-bar {
    position: absolute; left: 26px; top: 150px; width: 252px; height: 23px;
    background: var(--brand-red); color: #fff; text-align: center;
    font-size: 12px; font-weight: 500; letter-spacing: 1.6px; line-height: 23px;
  }
  .slide-title .halo { left: 298px; top: 44px; width: 186px; height: 186px; }
  .slide-title .photo { left: 321px; top: 33px; width: 132px; height: 190px; border-radius: 40% 40% 20% 20%;
    background: linear-gradient(180deg, var(--photo-warm), #e7ddd3); }
  .tagline { position: absolute; left: 310px; top: 226px; width: 155px; text-align: center;
    font-family: "Caveat", cursive; font-size: 15px; color: var(--ink-dark); }

  /* Question slide */
  .slide-question { left: 23px; top: 460px; width: 283px; height: 158px; transform: rotate(-6deg); }
  .slide-question .halo { left: 20px; top: 55px; width: 88px; height: 88px; }
  .slide-question .photo { left: 30px; top: 40px; width: 66px; height: 100px; border-radius: 40%;
    background: linear-gradient(180deg, var(--photo-grey), #e1dcd6); }
  .slide-question .quote-mark.open { left: 118px; top: 34px; font-size: 22px; }
  .slide-question .quote-mark.close { left: 236px; top: 86px; font-size: 22px; }
  .slide-question .greeting { position: absolute; left: 130px; top: 40px; font-size: 10.5px; font-weight: 500; }
  .slide-question .ask { position: absolute; left: 130px; top: 70px; width: 130px; font-size: 9.5px; font-weight: 500; line-height: 13px; }
  .slide-question .brand { right: 10px; bottom: 8px; font-size: 7px; }
  .slide-question .brand-dot { width: 10px; height: 10px; }

  /* History slide */
  .slide-history { left: 331px; top: 432px; width: 316px; height: 172px; transform: rotate(10.8deg); }
  .slide-history .quote-mark.open { left: 44px; top: 26px; font-size: 24px; }
  .slide-history .quote-mark.close { left: 160px; top: 96px; font-size: 24px; }
  .slide-history .lead { position: absolute; left: 56px; top: 50px; width: 150px; font-size: 11px; font-weight: 500; line-height: 15px; }
  .slide-history .halo { left: 196px; top: 44px; width: 108px; height: 108px; }
  .slide-history .photo { left: 196px; top: 48px; width: 108px; height: 92px; border-radius: 30%;
    background: linear-gradient(180deg, #c9b49a, #efe9e2); }
  .slide-history .brand { right: 10px; bottom: 8px; font-size: 7px; }
  .slide-history .brand-dot { width: 10px; height: 10px; }

  /* Story slide */
  .slide-story { left: 35px; top: 641px; width: 441px; height: 245px; transform: rotate(-5.5deg); }
  .story-copy { position: absolute; left: 14px; top: 16px; width: 413px; text-align: center; font-size: 9.6px; font-weight: 500; line-height: 12px; }
  .story-copy p + p { margin-top: 12px; }
  .slide-story .photo { left: 120px; top: 168px; width: 210px; height: 62px; border-radius: 40% 40% 12% 12%;
    background: linear-gradient(90deg, #222, #8c8c8c 55%, #eee); }
  .slide-story .brand { right: 14px; bottom: 26px; font-size: 7px; }
  .slide-story .brand-dot { width: 10px; height: 10px; }

  /* Closing slide */
  .slide-close { left: 139px; top: 906px; width: 498px; height: 275px; }
  .slide-close .halo { left: 34px; top: 52px; width: 184px; height: 184px; }
  .slide-close .photo { left: 75px; top: 50px; width: 100px; height: 210px; border-radius: 45% 45% 30% 30%;
    background: linear-gradient(180deg, #8a5a36, #f3efea 40%); }
  .slide-close h2 { position: absolute; left: 211px; top: 42px; font-size: 34px; line-height: 36px; }
  .slide-close .quote-mark.open { left: 218px; top: 88px; font-size: 32px; }
  .slide-close .quote-mark.close { position: static; font-size: 30px; vertical-align: -10px; margin-left: 6px; }
  .closing-copy { position: absolute; left: 245px; top: 96px; width: 240px; font-size: 16px; line-height: 22.5px; }
  .slide-close .brand { right: 14px; bottom: 14px; font-size: 9px; }
  .slide-close .brand-dot { width: 14px; height: 14px; }
</style>
</head>
<body>
  <p class="board-note">Looking for your suggestions and let me know any edits to do<br>Thank you! Have a nice day!</p>

  <section class="slide slide-title">
    <div class="brand"><span class="brand-dot"></span>Omnis</div>
    <h1 class="display">Ask Professor Wembleton</h1>
    <div class="topic-bar">CANINE DIET AND LIFE SPAN</div>
    <div class="halo"></div>
    <div class="photo" role="img" aria-label="Photo of a basset hound wearing round glasses, sitting"></div>
    <p class="tagline">The World's Smartest Dog</p>
  </section>

  <section class="slide slide-question">
    <div class="halo"></div>
    <div class="photo" role="img" aria-label="Photo of a whippet wearing glasses"></div>
    <span class="quote-mark open">“</span>
    <p class="greeting">Professor Wembleton,</p>
    <p class="ask">How can dogs <span class="accent">live longer, healthier lives</span>?</p>
    <span class="quote-mark close">”</span>
    <div class="brand"><span class="brand-dot"></span>Omnis</div>
  </section>

  <section class="slide slide-history">
    <span class="quote-mark open">“</span>
    <p class="lead">Let's take a look at the history of <span class="accent">canine diets.</span></p>
    <span class="quote-mark close">”</span>
    <div class="halo"></div>
    <div class="photo" role="img" aria-label="Photo of a dog in glasses reading an open book among stacked books"></div>
    <div class="brand"><span class="brand-dot"></span>Omnis</div>
  </section>

  <section class="slide slide-story">
    <div class="story-copy">
      <p>The Effects of Modern Diets on Dogs Up until the modern age, the domestic dog ate what his master ate----bones and scraps from the family table----and enjoyed a long life, often spanning two decades.</p>
      <p>Since the 1950's, however dogs have been fed what cows ate---a corn-based diet. As a result, over 80% of modern dogs have gum disease and over half of dogs 10 or older will develop cancer.</p>
      <p>In the 1990's marketeers unscientifically pushed a wolf diet with too much protein and too little fiber, causing dogs to become overweight and yet still be hungry.</p>
    </div>
    <div class="photo" role="img" aria-label="Photo of a black and white dog lying down looking sad"></div>
    <div class="brand"><span class="brand-dot"></span>Omnis</div>
  </section>

  <section class="slide slide-close">
    <div class="halo"></div>
    <div class="photo" role="img" aria-label="Photo of a happy Jack Russell terrier sitting with a red collar"></div>
    <h2 class="display">Professor Wembleton Says</h2>
    <span class="quote-mark open">“</span>
    <p class="closing-copy">Join the <span class="accent">Omnis Superfood Revolution</span> today! Give your pet the food best formulated to satisfy the total dog.<span class="quote-mark close">”</span></p>
    <div class="brand"><span class="brand-dot"></span>Omnis</div>
  </section>
</body>
</html>
```